Invitation Design for TORAM KELPANE Investigator Event (Exclusive Cocktail Reception)

Project Overview:
Toram Cellworks is hosting an exclusive, invitation-only cocktail reception for KELPANE clinical study investigators during the ODRIM 2026 Conference. We need a polished, high-end event invitation designed for both email and print formats.
Event Details:
Event Name: Gather & Grow: The KELPANE Investigator Event
Date: Saturday, January 24
Time: 5:00–7:00 PM
Location: Walter Brisk Chophouse (Hartwell Private Room), Orlean Terrace
Purpose: A relaxed, come-and-go cocktail reception for KELPANE investigators to mingle; light content and conversation, no formal presentations.
Design Requirements:
Two logos required:
TORAM (primary)
KELPANE (secondary)
Color Palette: Use the Toram color scheme, KELPANE color scheme, or a clean blend of both.
Tone & Style: Premium, modern, medical-professional with a high-end reception feel
Deliverable Layout:
Event title
Date & time
Location
Blurb: You are invited to a gathering for KELPANE clinical investigators. This event is intended to provide an opportunity for professional discussion, study related updates, and peer connection within the investigator community.
Both required logos
Clean, elegant spacing with strong hierarchy
What We Want
A visually striking but clean design that feels:
Sophisticated and corporate-professional
Consistent with our brand aesthetic
Appropriate for a high-profile physician audience
Think: elevated, clinical, modern — not flashy or overly busy.
Audience
Physicians and researchers participating in the KELPANE clinical study — a high-end, professional group.

```html
<!DOCTYPE html>
<html lang="en">
<head>
<meta charset="utf-8">
<title>Gather &amp; Grow: The KELPANE Investigator Event</title>
<link rel="stylesheet" href="https://fonts.googleapis.com/css2?family=Exo+2:ital,wght@0,300;0,400;1,300&display=swap">
<style>
  :root {
    --navy: #020b2e;
    --green: #6db33f;
    --white: #ffffff;
    --violet: #5a4a86;
  }
  html, body {
    margin: 0;
    padding: 0;
    width: 960px;
    height: 1200px;
    overflow: hidden;
    background: var(--navy);
  }
  .invitation {
    position: relative;
    width: 960px;
    height: 1200px;
    background: var(--navy);
    color: var(--white);
    font-family: "Exo 2", sans-serif;
  }
  .brand-primary {
    position: absolute;
    left: 60px;
    top: 40px;
    margin: 0;
    font-weight: 400;
    font-size: 74px;
    line-height: 1;
    letter-spacing: -1px;
    color: var(--green);
  }
  .brand-study {
    position: absolute;
    right: 56px;
    top: 50px;
    display: flex;
    align-items: center;
    gap: 14px;
    margin: 0;
    font-weight: 400;
    font-size: 52px;
    line-height: 1;
    color: var(--white);
  }
  .brand-study__mark {
    width: 26px;
    height: 26px;
    background: var(--white);
  }
  .event-title {
    position: absolute;
    top: 222px;
    left: 0;
    width: 960px;
    margin: 0;
    text-align: center;
    font-weight: 400;
    font-size: 96px;
    line-height: 1;
    color: var(--white);
  }
  .event-subtitle {
    position: absolute;
    top: 335px;
    left: 0;
    width: 960px;
    margin: 0;
    text-align: center;
    font-weight: 300;
    font-size: 42px;
    line-height: 1;
    color: var(--green);
  }
  .event-blurb {
    position: absolute;
    top: 420px;
    left: 200px;
    width: 560px;
    margin: 0;
    text-align: center;
    font-style: italic;
    font-weight: 300;
    font-size: 23px;
    line-height: 30.5px;
    color: var(--white);
  }
  .wave-artwork {
    position: absolute;
    left: 0;
    top: 585px;
    width: 960px;
    height: 440px;
    background:
      radial-gradient(ellipse 45% 40% at 28% 40%, rgba(109,179,63,0.22), transparent 70%),
      radial-gradient(ellipse 40% 35% at 45% 55%, rgba(90,74,134,0.28), transparent 70%),
      radial-gradient(ellipse 50% 20% at 80% 52%, rgba(109,179,63,0.18), transparent 70%),
      var(--navy);
  }
  .event-details {
    position: absolute;
    left: 0;
    top: 1050px;
    width: 960px;
    height: 90px;
  }
  .detail {
    position: absolute;
    display: flex;
    align-items: center;
    font-weight: 400;
    font-size: 27px;
    line-height: 29px;
    color: var(--white);
  }
  .detail--when { left: 74px; top: 8px; }
  .detail--where { left: 486px; top: 0; }
  .detail__icon { flex: none; }
  .detail--when .detail__text { margin-left: 32px; }
  .detail--where .detail__text { margin-left: 26px; }
  .detail__text p { margin: 0; }
</style>
</head>
<body>
<main class="invitation">
  <header>
    <p class="brand-primary">TORAM</p>
    <p class="brand-study"><span class="brand-study__mark"></span>KELPANE</p>
  </header>

  <h1 class="event-title">Gather &amp; Grow:</h1>
  <h2 class="event-subtitle">The KELPANE Investigator Event</h2>

  <p class="event-blurb">You are invited to a gathering for KELPANE clinical investigators. This event is intended to provide an opportunity for professional discussion, study related updates, and peer connection within the investigator community.</p>

  <div class="wave-artwork" role="img" aria-label="Flowing green and violet line-wave ribbons sweeping across the card"></div>

  <section class="event-details">
    <div class="detail detail--when">
      <svg class="detail__icon" width="76" height="76" viewBox="0 0 76 76" fill="none" stroke="#6db33f" stroke-width="3" stroke-linecap="round">
        <circle cx="38" cy="38" r="35"/>
        <path d="M38 8v6M38 62v6M8 38h6M62 38h6M17 17l4 4M55 17l-4 4M17 59l4-4M55 59l-4-4"/>
        <path d="M38 38V20M38 38l10-9"/>
      </svg>
      <div class="detail__text">
        <p>Saturday, January 24</p>
        <p>5:00–7:00 PM</p>
      </div>
    </div>
    <div class="detail detail--where">
      <svg class="detail__icon" width="56" height="84" viewBox="0 0 56 84" fill="none" stroke="#6db33f" stroke-width="3" stroke-linejoin="round">
        <path d="M28 81C14 58 3 43 3 28a25 25 0 0 1 50 0c0 15-11 30-25 53z"/>
        <circle cx="28" cy="27" r="8"/>
      </svg>
      <div class="detail__text">
        <p>Walter Brisk Chophouse</p>
        <p>(Hartwell Private Room),</p>
        <p>Orlean Terrace</p>
      </div>
    </div>
  </section>
</main>
</body>
</html>
```